Celling poster

It is a celling poster with questions that you ask yourself in the morning and a morning prayer + evening questions. People might put it on celling or on the wall.

Here is the contant, it is in Slovenian, but I have send you translation.

PO JUTRU SE DAN POZNA ...

1. Kaj me trenutno najbolj veseli v življenju?
3. Na kaj sem ponosna v življenju?
4. Za katere stvari danes čutim največ hvaležnosti?
5. V čem trenutno najbolj uživam?
6. Koga imam rada in kdo me ima rad?

Danes vstajam
s pomočjo nebeških sil:
svetlobe sonca,
sija lune,
žara ognja,
hitrosti strele,
okretnosti vetra,
globine morja,
stanovitnosti zemlje,
trdnosti skale.

VEČERNE MODROSTI

1. Kaj je bil danes moj prispevek svetu?
2. Kaj sem se danes naučila?
3. Katera situacija v dnevu mi je prinesla največ občutkov topline?

TRANSLATION for your understanding.

MORNING POWER QUESTIONS
1. What am I happy abou in my life right now?
2. What am I excited about in my life now?
3. What am I proud about in my life now?
4. What am I grateful about in my life now?
5. What am I enjoying most in my life now?
6. Who do I love? Who loves me?

MORNING PRAYER
Today I am waking up with the power of heavenly forces.
With the light of sun,
light of moon,
light of fire,
speed of lightning,
flexibility of wind,
depps of ocean,
stability of earth and
hardness of rock.

EVENING QUESTIONS OF WISDOM
1. What have I given today?
2. What did I learn today?
3. Which situations today gave me the most feelings of love, warmth?

```html
<!DOCTYPE html>
<html lang="sl">
<head>
<meta charset="utf-8">
<title>Po jutru se dan pozna – plakat</title>
<link rel="stylesheet" href="https://fonts.googleapis.com/css2?family=Righteous&family=Roboto:wght@700&family=Kaushan+Script&family=Dancing+Script:wght@400&display=swap">
<style>
  :root{
    --page:#ece8e2;
    --orange:#f26c23;
    --amber:#f8a21a;
    --sun:#fed40c;
    --pale:#fdf0b0;
    --mist:#dfe9ef;
    --sky-blue:#5d9ec7;
    --deep-blue:#2c5f92;
    --navy:#0b0d2c;
    --ink:#121018;
    --white:#ffffff;
  }
  *{margin:0;padding:0;box-sizing:border-box}
  html,body{width:1200px;height:1200px;overflow:hidden;background:var(--page)}
  .poster{
    position:absolute;left:180px;top:40px;width:841px;height:1120px;overflow:hidden;
    background:linear-gradient(180deg,var(--orange) 0%,var(--amber) 24%,var(--sun) 42%,var(--pale) 56%,var(--mist) 62%,var(--sky-blue) 70%,var(--deep-blue) 78%,var(--navy) 88%,var(--navy) 100%);
    box-shadow:0 10px 30px rgba(0,0,0,.25);
  }
  .sun-glow{
    position:absolute;left:253px;top:378px;width:320px;height:320px;border-radius:50%;
    background:radial-gradient(circle,rgba(255,247,205,.7) 0%,rgba(255,242,180,.5) 65%,rgba(255,238,160,0) 100%);
  }
  .mountain-mist{
    position:absolute;left:0;top:640px;width:100%;height:300px;
    background:linear-gradient(180deg,rgba(190,215,230,0) 0%,rgba(170,205,225,.55) 25%,rgba(90,150,195,.55) 55%,rgba(11,13,44,0) 100%);
  }
  .morning-title{
    position:absolute;left:103px;top:60px;font-family:"Righteous",sans-serif;font-size:51px;
    color:var(--ink);letter-spacing:-1px;white-space:nowrap;
  }
  .question-list{
    position:absolute;list-style:none;font-family:"Roboto",sans-serif;font-weight:700;
    font-size:23px;white-space:nowrap;
  }
  .question-list.morning{left:163px;top:131px;color:var(--ink);line-height:27.7px}
  .question-list.evening{left:67px;top:957px;color:var(--white);line-height:37.3px}
  .prayer-title{
    position:absolute;left:0;width:838px;top:311px;text-align:center;
    font-family:"Righteous",sans-serif;font-size:61px;color:var(--ink);letter-spacing:-1px;
  }
  .prayer{
    position:absolute;left:0;width:826px;top:404px;text-align:center;color:var(--ink);
  }
  .prayer .lead{font-family:"Kaushan Script",cursive;font-size:38px;line-height:45px}
  .prayer .forces{list-style:none;font-family:"Dancing Script",cursive;font-size:34px;line-height:39.4px;margin-top:2px}
  .evening-title{
    position:absolute;left:67px;top:870px;font-family:"Righteous",sans-serif;font-size:54px;
    color:var(--white);letter-spacing:-1px;white-space:nowrap;
  }
  .question-bubbles{
    position:absolute;left:575px;top:872px;width:200px;height:165px;
    background:radial-gradient(ellipse 50% 50% at 50% 50%,rgba(248,170,60,.85) 0%,rgba(246,150,50,.55) 45%,rgba(11,13,44,0) 100%);
  }
</style>
</head>
<body>
  <main class="poster">
    <div class="sun-glow"></div>
    <div class="mountain-mist" role="img" aria-label="Modre gore v jutranji megli"></div>

    <h1 class="morning-title">PO JUTRU SE DAN POZNA ...</h1>
    <ol class="question-list morning">
      <li>1. Kaj me trenutno najbolj veseli v življenju?</li>
      <li>3. Na kaj sem ponosna v življenju?</li>
      <li>4. Za katere stvari danes čutim največ hvaležnosti?</li>
      <li>5. V čem trenutno najbolj uživam?</li>
      <li>6. Koga imam rada in kdo me ima rad?</li>
    </ol>

    <h2 class="prayer-title">Danes vstajam</h2>
    <div class="prayer">
      <p class="lead">s pomočjo<br>nebeških sil:</p>
      <ul class="forces">
        <li>svetlobe sonca,</li>
        <li>sija lune,</li>
        <li>žara ognja,</li>
        <li>hitrosti strele,</li>
        <li>okretnosti vetra,</li>
        <li>globine morja,</li>
        <li>stanovitnosti zemlje,</li>
        <li>trdnosti skale.</li>
      </ul>
    </div>

    <h2 class="evening-title">VEČERNE MODROSTI</h2>
    <div class="question-bubbles" role="img" aria-label="Barvni oblački z vprašaji"></div>
    <ol class="question-list evening">
      <li>1. Kaj je bil danes moj prispevek svetu?</li>
      <li>2. Kaj sem se danes naučila?</li>
      <li>3. Katera situacija v dnevu mi je prinesla največ občutkov topline?</li>
    </ol>
  </main>
</body>
</html>
```